PWR Business Card

Looking for a business card for my restaurant group I own. Four different concepts:

Copperleaf Alehouse
Bramble Alehouse
Hollister's Wood Fired Grill
Fenwick Patty Company

Card doesn't need to include all the logos.

```html
<!DOCTYPE html>
<html lang="en">
<head>
<meta charset="utf-8">
<title>PWR Business Card</title>
<link href="https://fonts.googleapis.com/css2?family=Montserrat:wght@400;500;600&display=swap" rel="stylesheet">
<style>
  :root {
    --page: #e9e6e1;
    --white: #ffffff;
    --gold: #c9a04a;
    --grey: #6b6b6d;
    --grey-dark: #5c5c5e;
    --grey-light: #77777a;
    --text: #555558;
    --divider: #c9c9cc;
    --bullet: #e0893a;
  }
  * { box-sizing: border-box; margin: 0; padding: 0; }
  html, body { width: 900px; height: 1200px; overflow: hidden; }
  body {
    background: var(--page);
    font-family: "Montserrat", sans-serif;
    position: relative;
  }
  .card {
    position: absolute;
    left: 80px;
    width: 740px;
    height: 420px;
    box-shadow: 0 6px 18px rgba(0,0,0,0.18);
    overflow: hidden;
  }
  .card--front { top: 140px; background: var(--white); }
  .card--back { top: 640px; background: var(--grey); }

  .front-main { position: absolute; inset: 0 0 110px 0; }
  .brand {
    position: absolute;
    left: 70px; top: 80px;
    width: 250px;
    color: var(--gold);
    font-weight: 500;
    text-align: center;
  }
  .brand__initials { font-size: 62px; letter-spacing: 4px; line-height: 1; }
  .brand__name { font-size: 19px; letter-spacing: 3px; margin-top: 14px; line-height: 1.35; }
  .divider {
    position: absolute;
    left: 352px; top: 60px;
    width: 1px; height: 190px;
    background: var(--divider);
  }
  .contact { position: absolute; left: 382px; top: 66px; color: var(--text); }
  .contact__name { color: var(--gold); font-size: 27px; font-weight: 500; letter-spacing: 1px; }
  .contact__role { font-size: 17px; margin-top: 4px; }
  .contact__list { list-style: none; margin-top: 22px; }
  .contact__list li { display: flex; align-items: center; font-size: 15px; margin-bottom: 12px; }
  .contact__list svg { width: 18px; height: 18px; margin-right: 14px; fill: var(--gold); flex: none; }

  .concepts {
    position: absolute;
    left: 0; right: 0; bottom: 0;
    height: 110px;
    background: var(--grey);
    color: var(--white);
    font-size: 15px;
    display: flex; flex-wrap: wrap; justify-content: center; align-content: center;
    gap: 10px 26px;
    padding: 0 40px;
    list-style: none;
  }
  .concepts li { display: flex; align-items: center; }
  .concepts li::before {
    content: ""; width: 7px; height: 7px; border-radius: 50%;
    background: var(--bullet); margin-right: 9px;
  }
  .concepts__break { flex-basis: 100%; height: 0; }

  .back-pattern {
    position: absolute; inset: 0;
    background: linear-gradient(180deg, var(--grey-light), var(--grey) 60%, var(--grey-dark));
  }
  .back-footer {
    position: absolute; right: 48px; bottom: 40px;
    display: flex; align-items: center; gap: 22px;
  }
  .back-footer__web { color: var(--white); font-size: 17px; }
  .back-footer__mark { color: var(--gold); font-size: 34px; font-weight: 500; letter-spacing: 3px; }
</style>
</head>
<body>
  <section class="card card--front">
    <div class="front-main">
      <div class="brand">
        <div class="brand__initials">PWR</div>
        <div class="brand__name">PINEWATER<br>HOSPITALITY GROUP</div>
      </div>
      <div class="divider"></div>
      <div class="contact">
        <div class="contact__name">MARISA DELCOURT</div>
        <div class="contact__role">Owner</div>
        <ul class="contact__list">
          <li><svg viewBox="0 0 24 24" aria-hidden="true"><path d="M6.6 10.8a15.1 15.1 0 0 0 6.6 6.6l2.2-2.2c.3-.3.7-.4 1-.2 1.1.4 2.3.6 3.6.6.6 0 1 .4 1 1V20c0 .6-.4 1-1 1A17 17 0 0 1 3 4c0-.6.4-1 1-1h3.5c.6 0 1 .4 1 1 0 1.3.2 2.5.6 3.6.1.3 0 .7-.2 1z"/></svg>555.218.4470</li>
          <li><svg viewBox="0 0 24 24" aria-hidden="true"><circle cx="12" cy="12" r="10"/></svg>marisadelcourt@mail.com</li>
          <li><svg viewBox="0 0 24 24" aria-hidden="true"><path d="M12 2a10 10 0 1 0 0 20 10 10 0 0 0 0-20zm6.9 6h-3a15.7 15.7 0 0 0-1.3-3.6A8 8 0 0 1 18.9 8zM12 4c.8 1.2 1.5 2.5 1.9 4h-3.8c.4-1.5 1.1-2.8 1.9-4zM4.3 14a8 8 0 0 1 0-4h3.4a16.5 16.5 0 0 0 0 4zm.8 2h3c.3 1.3.8 2.5 1.3 3.6A8 8 0 0 1 5.1 16zm3-8h-3a8 8 0 0 1 4.3-3.6C8.9 5.5 8.4 6.7 8.1 8zM12 20c-.8-1.2-1.5-2.5-1.9-4h3.8c-.4 1.5-1.1 2.8-1.9 4zm2.3-6H9.7a14.7 14.7 0 0 1 0-4h4.6a14.7 14.7 0 0 1 0 4zm.3 5.6c.5-1.1 1-2.3 1.3-3.6h3a8 8 0 0 1-4.3 3.6zm1.7-5.6a16.5 16.5 0 0 0 0-4h3.4a8 8 0 0 1 0 4z"/></svg>www.pinewaterhospitality.com</li>
        </ul>
      </div>
    </div>
    <ul class="concepts">
      <li>Copperleaf Alehouse</li>
      <li>Bramble Alehouse</li>
      <li>Hollister's Wood Fired Grill</li>
      <span class="concepts__break"></span>
      <li>Fenwick Patty Company</li>
    </ul>
  </section>

  <section class="card card--back">
    <div class="back-pattern" role="img" aria-label="Faint repeating brand pattern in grey tones"></div>
    <div class="back-footer">
      <span class="back-footer__web">www.pinewaterhospitality.com</span>
      <span class="back-footer__mark">PWR</span>
    </div>
  </section>
</body>
</html>
```